High-end Oceanfront Real Estate Group Needs Clean, Modern Web Design

I’m looking for a clean, professional, modern and beautiful homepage web design for a Real Estate group in Southern California, USA.

The group/company is “Marlow on the Tide,” and they specialize in high end (i.e. expensive), oceanfront real estate in the Orange County area.

The look and feel of the page should accentuate the brand qualities: luxurious/expensive, professional, and beautiful (Orange County is one of the most beautiful areas in all the US and we would love the site to emphasize the beautiful beaches and scenery it has to offer).

Looks we like:
• www.brantleyhomesrealty.example
• www.keptbyvane.example -- I think the design is pretty out-dated in this site, but I like the organization/layout of the site

Header Tags (I don’t know if we can fit all of these, may need a side-menu, but I’d prefer header title only if possible):
• Welcome
• Featured Listings
• Previously Sold
• Sell
• Property Search
• Team
• Videos
• Blog
• Explore O.C.
• Contact

I have attached the beach and logo pics that we would like to use as the header, a few pictures of the team, and one sample home/view pic which can be used in any of the other sections (for pictures of the homes, just find expensive oceanfront houses and that will be fine).

I promise to provide feedback to each and every design submission. I appreciate the hard work that all of you are putting into your designs. There can be only one contest winner, but I hope to give all of you helpful feedback to submit the best designs possible!

Target Market(s)

Very wealthy home owners of oceanfront properties. These properties are worth several millions of dollars, and thus the site and brand needs to be targeted to very wealthy, successful individuals and families (both US and international buyers).

Industry/Entity Type

Real Estate

Number of Pages Required

2 page

Requirements
Must have
• I don’t want to give too many requirements, because I want to let you all be creative. However, here are the few Must Haves:
• Must submit 2 page designs (a home page and a sub page)
• Must use logo provided
• Focus is mostly on homes, but I would like to include some beach/ocean imagery as well
• The first “item” on the home page should be an accordion/slider which shows pictures of homes and with 1 line of text: “List with the Leader” and two link buttons: “Sell Your Home” and “Buy Your Home”
• Color palette needs to be mainly blues--to match ocean and sky blue
• Exported in all major formats (psd,ai,eps,png,jpeg,etc)
Nice to have
• We don’t necessarily need all of these, but would like to feature most:
• List of videos
• “Meet the Team”—brief team bios and pics
• Link(s) to Blog
• “List with the Leader” – section on why they should choose this firm
• Featured Listings
• Previously Sold

```html
<!DOCTYPE html>
<html lang="en">
<head>
<meta charset="utf-8">
<title>Marlow on the Tide — Oceanfront Real Estate</title>
<link rel="stylesheet" href="https://fonts.googleapis.com/css2?family=Raleway:wght@200;300;400;500;600&family=Lora:ital@1&display=swap">
<style>
:root{
  --blue:#26a9e8;
  --blue-dark:#1590cf;
  --ink:#2e2e2e;
  --text:#6b6b6b;
  --muted:#a3a3a3;
  --rule:#e4e4e4;
  --side-bg:#f2f2f2;
  --nav-bg:#eef0f3;
  --footer-bg:#14171c;
  --footer-text:#8d939b;
  --white:#ffffff;
}
*{margin:0;padding:0;box-sizing:border-box}
html,body{width:1200px;height:2209px;overflow:hidden;background:var(--white)}
body{position:relative;font-family:"Raleway",sans-serif;color:var(--text)}
h1,h2,h3,h4,h5{font-weight:400}
.abs{position:absolute}
.photo{box-shadow:inset 0 0 40px rgba(0,0,0,.18)}

/* hero */
.hero{left:0;top:0;width:1200px;height:607px;
  background:
    radial-gradient(ellipse 420px 90px at 78% 16%,rgba(255,255,255,.45),transparent 70%),
    radial-gradient(ellipse 360px 70px at 22% 26%,rgba(255,255,255,.35),transparent 70%),
    linear-gradient(90deg,transparent 70%,rgba(235,225,210,.35) 85%,rgba(200,120,90,.25) 100%),
    linear-gradient(180deg,#25467f 0%,#3f66a3 14%,#7fa2cc 28%,#b9cde0 41%,#8aa3b5 45%,#5c7687 47%,#2e4a36 52%,#1f3820 62%,#2f4d25 72%,#4f7a33 84%,#3a5a2a 92%,#2b3f22 100%)}
.nav{left:100px;top:0;width:1001px;height:84px;background:var(--nav-bg);display:flex;box-shadow:0 3px 6px rgba(0,0,0,.25)}
.brand{width:125px;flex:none;display:flex;align-items:center;justify-content:center;padding:0 10px;
  font-weight:300;color:#5f7da3;font-size:18px;line-height:1.1;text-align:center}
.menu{display:flex;list-style:none;align-items:stretch;flex:1;justify-content:space-between;padding-right:10px}
.menu li{display:flex;align-items:center;padding:0 8px;font-size:12.5px;color:#3a3a3a;white-space:nowrap}
.menu li.active{background:var(--blue);color:var(--white);padding:0 22px}
.hero-title{left:0;width:1200px;top:230px;text-align:center;font-weight:200;font-size:46px;letter-spacing:2px;color:var(--white)}
.btn-sell,.btn-buy{top:315px;height:44px;display:flex;align-items:center;justify-content:center;font-size:16px;font-weight:500;color:var(--white);letter-spacing:.5px;white-space:nowrap}
.btn-sell{left:392px;width:182px;background:var(--blue)}
.btn-buy{left:589px;width:181px;border:2px solid var(--white);background:rgba(0,0,0,.15)}
.arrow{top:299px;width:35px;height:44px;background:rgba(20,20,20,.75);display:flex;align-items:center;justify-content:center}

/* sidebar */
.sidebar{left:99px;top:608px;width:215px;height:1329px;background:var(--side-bg)}
.side-head{left:99px;width:215px;height:41px;background:var(--blue);color:var(--white);font-size:16px;display:flex;align-items:center;justify-content:center;letter-spacing:.5px}
.blog-item{left:99px;width:215px;height:85px;border-bottom:1px solid #e2e2e2;padding:12px 16px 0 17px}
.blog-item p{font-size:12.5px;line-height:18px;color:#666}
.blog-item time{display:block;margin-top:6px;font-size:11px;color:var(--blue);font-weight:600}
.read-more{left:122px;top:915px;font-size:12px;font-weight:500;color:#333}
.side-quote{left:117px;top:1007px;width:190px;font-family:"Lora",serif;font-style:italic;font-size:15px;line-height:21px;color:#555}
.side-photo{left:118px;width:177px;height:120px;border:3px solid var(--white);outline:1px solid #d6d6d6}
.side-text{left:117px;width:185px;font-size:12.5px;line-height:19px;color:#666}
.price{font-family:"Lora",serif;font-style:italic;color:var(--blue)}

/* main */
.sec-title{left:355px;font-size:23px;color:var(--ink);letter-spacing:.5px}
.sec-intro{left:355px;width:745px;font-size:15.5px;line-height:22px;color:#666}
.video{left:353px;top:751px;width:748px;height:233px;
  background:
    radial-gradient(ellipse 200px 50px at 30% 18%,rgba(255,255,255,.45),transparent 70%),
    linear-gradient(90deg,transparent 52%,rgba(190,70,60,.35) 62%,rgba(240,228,205,.6) 78%,rgba(120,150,90,.45) 100%),
    linear-gradient(180deg,#2c5fb4 0%,#5c8fd6 30%,#b8d2ee 48%,#5fb0cc 52%,#3d93b4 64%,#9cc2c8 70%,#e0c49c 74%,#c99766 100%)}
.play{left:690px;top:828px}
.thumb{top:996px;width:83px;height:67px}
.rule{left:353px;width:748px;height:1px;background:var(--rule)}
.card-photo{top:1241px;width:230px;height:191px;border:3px solid var(--white);outline:1px solid #cfcfcf}
.card-title{top:1444px;width:230px;text-align:center;font-size:14.5px;color:var(--ink);white-space:nowrap}
.card-meta{top:1467px;width:230px;text-align:center;font-size:11.5px;color:var(--muted);white-space:nowrap}
.card-price{top:1485px;width:230px;text-align:center;font-size:14px}
.card-btn{top:1532px;width:84px;height:35px;background:var(--blue);color:var(--white);font-size:11px;font-weight:600;display:flex;align-items:center;justify-content:center;box-shadow:0 2px 0 var(--blue-dark)}
.member-photo{top:1748px;width:168px;height:142px;border:3px solid var(--white);outline:1px solid #cfcfcf}
.member-name{top:1900px;width:168px;text-align:center;font-size:13px;color:var(--ink)}
.member-role{top:1917px;width:168px;text-align:center;font-family:"Lora",serif;font-style:italic;font-size:12px;color:var(--blue)}

/* footer */
.footer{left:0;top:1973px;width:1200px;height:236px;background:linear-gradient(180deg,#181c22,#101317)}
.foot-head{top:2016px;font-size:12.5px;font-weight:600;color:var(--blue);letter-spacing:.3px}
.foot-list{list-style:none;font-size:11px;color:var(--footer-text);line-height:14px}
.contact li{display:flex;align-items:center;gap:10px;height:29px}
.contact svg{flex:none}
.tweet{font-size:11px;line-height:16px;color:var(--footer-text)}
.tweet em{color:var(--blue);font-size:10px}
.about li{height:24px}
.social{display:flex;gap:8px}
.social span{width:21px;height:21px;border-radius:50%;background:#565b62}
.social span.on{background:#d9d9d9}
.copy{left:932px;top:2168px;font-size:10.5px;color:#c9c9c9}
</style>
</head>
<body>

<section class="abs hero" role="img" aria-label="Oceanfront resort with palm trees, white colonnade and the coastline under a blue sky"></section>

<header class="abs nav">
  <div class="brand">Marlow on the Tide</div>
  <ul class="menu">
    <li class="active">HOME</li>
    <li>FEATURED LISTINGS</li>
    <li>PREVIOUSLY SOLD</li>
    <li>SELL</li>
    <li>SEARCH</li>
    <li>TEAM</li>
    <li>VIDEOS</li>
    <li>BLOG</li>
    <li>EXPLORE</li>
    <li>CONTACT</li>
  </ul>
</header>

<h1 class="abs hero-title">LIST WITH THE LEADER</h1>
<a class="abs btn-sell">SELL YOUR HOME</a>
<a class="abs btn-buy">BUY YOUR HOME</a>
<div class="abs arrow" style="left:0"><svg width="12" height="18" viewBox="0 0 12 18"><path d="M9 2 2 9l7 7" fill="none" stroke="#fff" stroke-width="2.5"/></svg></div>
<div class="abs arrow" style="left:1165px"><svg width="12" height="18" viewBox="0 0 12 18"><path d="m3 2 7 7-7 7" fill="none" stroke="#fff" stroke-width="2.5"/></svg></div>

<aside class="abs sidebar"></aside>
<h3 class="abs side-head" style="top:608px">OUR BLOG</h3>
<article class="abs blog-item" style="top:648px"><p>Sed ut pers lore piciatis unde omnis iste naloretus error</p><time>Feb 27, 2015</time></article>
<article class="abs blog-item" style="top:733px"><p>Sed ut pers lore piciatis unde omnis iste naloretus error</p><time>Feb 27, 2015</time></article>
<article class="abs blog-item" style="top:818px;border-bottom:none"><p>Sed ut pers lore piciatis unde omnis iste naloretus error</p><time>Feb 27, 2015</time></article>
<a class="abs read-more">READ MORE</a>

<h3 class="abs side-head" style="top:950px">LIST WITH THE LEADER</h3>
<p class="abs side-quote">Why they should choose this firm???</p>
<div class="abs side-photo photo" style="top:1063px;background:linear-gradient(90deg,#e9e2d2 0%,#c9b79a 22%,#8a5a3a 40%,#b8442e 55%,#5f8a4a 68%,#d8cfbf 80%,#f0ebe0 100%),#c9b79a;background-blend-mode:normal" role="img" aria-label="Home gym interior with wooden floor and bright windows"></div>
<p class="abs side-text" style="top:1208px">lorem ipsum dolor sit amet, consectetur adipiscing elit. Ut volutpat rutrum eros sit amet sollicitudin louspendisse.</p>

<h3 class="abs side-head" style="top:1305px">PREVIOUSLY SOLD</h3>
<div class="abs side-photo photo" style="top:1364px;background:linear-gradient(180deg,#2d6fd0 0%,#7fb0ea 40%,#c7ddf0 52%,#3f95bf 58%,#2f7fa8 68%,#8fb06a 78%,#3fb3d8 88%,#2a9cc4 100%)" role="img" aria-label="Oceanfront terrace with pool overlooking the sea"></div>
<p class="abs side-text" style="top:1500px">lorem ipsum dolor sit amet, consectetur <span class="price">$11,888,888</span></p>
<div class="abs side-photo photo" style="top:1555px;background:linear-gradient(180deg,#4a3020 0%,#8f6a48 35%,#c79a68 55%,#2a3f9a 72%,#3550b8 82%,#5a3e2a 100%)" role="img" aria-label="Dining room with chandeliers and blue chairs"></div>
<p class="abs side-text" style="top:1691px">lorem ipsum dolor sit amet, consectetur <span class="price">$11,888,888</span></p>
<div class="abs side-photo photo" style="top:1745px;background:linear-gradient(90deg,#6b5a48 0%,#b9a68a 25%,#e8eef2 42%,#cfdbe4 58%,#b9a68a 75%,#6b5a48 100%)" role="img" aria-label="Bright living room with tall windows"></div>
<p class="abs side-text" style="top:1880px">lorem ipsum dolor sit amet, consectetur <span class="price">$11,888,888</span></p>

<h2 class="abs sec-title" style="top:642px">OUR VIDEO’S</h2>
<p class="abs sec-intro" style="top:684px">lorem ipsum dolor sit amet, consectetur adipiscing elit. Ut volutpat rutrum eros sit amet sollicitudin. Suspendisse pulvinar, velit nec pharetar, velit nec pharet ra interdumante.</p>
<div class="abs video photo" role="img" aria-label="Beach house with red roof beside a pier and the ocean"></div>
<svg class="abs play" width="80" height="80" viewBox="0 0 80 80"><circle cx="40" cy="40" r="36" fill="rgba(0,0,0,.25)" stroke="#fff" stroke-width="4"/><circle cx="40" cy="40" r="28" fill="#fff"/><path d="M34 28v24l19-12z" fill="#333"/></svg>
<div class="abs thumb photo" style="left:355px;background:linear-gradient(180deg,#4f86d0 0%,#9cc0e8 45%,#3aa0c0 60%,#c89a6a 100%)" role="img" aria-label="Beach house thumbnail"></div>
<div class="abs thumb photo" style="left:449px;background:linear-gradient(180deg,#5a90d8 0%,#a7c8ec 45%,#3aa0c0 60%,#c08a5e 100%)" role="img" aria-label="Beach house thumbnail"></div>
<div class="abs thumb photo" style="left:543px;background:linear-gradient(180deg,#a9c0d6 0%,#dfe6ec 35%,#6f8a9a 55%,#4f6a46 100%)" role="img" aria-label="Coastal home thumbnail"></div>
<div class="abs thumb photo" style="left:637px;background:linear-gradient(180deg,#7fa6cf 0%,#c6d8ea 40%,#a2523e 60%,#5a3a2e 100%)" role="img" aria-label="Seaside villa thumbnail"></div>
<div class="abs thumb photo" style="left:731px;background:linear-gradient(180deg,#eef1f4 0%,#c8d0d8 45%,#5e6e7a 70%,#2f3a44 100%)" role="img" aria-label="Modern interior thumbnail"></div>
<div class="abs thumb photo" style="left:825px;background:linear-gradient(180deg,#a9d08a 0%,#e6d0a8 45%,#d8a070 70%,#6e9a4a 100%)" role="img" aria-label="Family on the lawn thumbnail"></div>
<div class="abs thumb photo" style="left:919px;background:linear-gradient(180deg,#4f8fd8 0%,#a9cdee 45%,#3aa0c0 55%,#ece6d6 70%,#d9d2c0 100%)" role="img" aria-label="Beach shoreline thumbnail"></div>
<div class="abs thumb photo" style="left:1013px;background:linear-gradient(180deg,#b9cfe6 0%,#dfe8f0 35%,#7fa2bc 60%,#4f6a7c 100%)" role="img" aria-label="Blue house thumbnail"></div>

<div class="abs rule" style="top:1097px"></div>

<h2 class="abs sec-title" style="top:1122px">FEATURED LISTINGS</h2>
<p class="abs sec-intro" style="top:1164px">lorem ipsum dolor sit amet, consectetur adipiscing elit. Ut volutpat rutrum eros sit amet sollicitudin. Suspendisse pulvinar, velit nec pharetar, velit nec pharet ra interdumante.</p>

<div class="abs card-photo photo" style="left:355px;background:radial-gradient(ellipse 60px 50px at 50% 42%,rgba(200,225,240,.9),transparent 80%),linear-gradient(180deg,#5a2e16 0%,#9a5a2e 30%,#d49a5a 48%,#6e3a1c 70%,#2a160c 100%)" role="img" aria-label="Dining room with an ocean view through the windows"></div>
<h4 class="abs card-title" style="left:355px">14 Tidewater, Emerald Bay</h4>
<p class="abs card-meta" style="left:355px">Bedrooms: 12 &nbsp; Bathrooms: 5 full | 18</p>
<p class="abs card-price price" style="left:355px">$11,888,888</p>
<a class="abs card-btn" style="left:428px">READ MORE</a>

<div class="abs card-photo photo" style="left:613px;background:radial-gradient(ellipse 70px 80px at 50% 55%,rgba(120,70,40,.7),transparent 80%),linear-gradient(180deg,#3c6fb3 0%,#8fb3dc 18%,#e2c08a 38%,#c9955a 60%,#5f8a3e 82%,#3e6a2a 100%)" role="img" aria-label="Mediterranean estate entrance with a fountain"></div>
<h4 class="abs card-title" style="left:613px">Luxury Real Estate Sales</h4>
<p class="abs card-meta" style="left:613px">Bedrooms: 12 &nbsp; Bathrooms: 5 full | 18</p>
<p class="abs card-price price" style="left:613px">$11,888,888</p>
<a class="abs card-btn" style="left:686px">READ MORE</a>

<div class="abs card-photo photo" style="left:869px;background:linear-gradient(180deg,#3f83cf 0%,#a9cbec 30%,#e8d6b4 45%,#c8a57a 62%,#eef0ee 72%,#5f7a3c 86%,#3f5a2a 100%)" role="img" aria-label="Large coastal house with garage and garden"></div>
<h4 class="abs card-title" style="left:869px">14 Tidewater, Emerald Bay</h4>
<p class="abs card-meta" style="left:869px">Bedrooms: 12 &nbsp; Bathrooms: 5 full | 18</p>
<p class="abs card-price price" style="left:869px">$11,888,888</p>
<a class="abs card-btn" style="left:942px">READ MORE</a>

<div class="abs rule" style="top:1608px"></div>

<h2 class="abs sec-title" style="top:1633px">MEET THE TEAM</h2>
<p class="abs sec-intro" style="top:1675px">lorem ipsum dolor sit amet, consectetur adipiscing elit. Ut volutpat rutrum eros sit amet sollicitudin. Suspendisse pulvinar, velit nec pharetar, velit nec pharet ra interdumante.</p>

<div class="abs member-photo" style="left:355px;background:linear-gradient(180deg,#6f98c8,#a7c0dc 60%,#d9c0a6)" role="img" aria-label="Portrait of a sales partner"></div>
<p class="abs member-name" style="left:355px">Dana Whitlow</p>
<p class="abs member-role" style="left:355px">Sales Partner</p>

<div class="abs member-photo" style="left:548px;background:linear-gradient(180deg,#e6e6e6,#bdbdbd 55%,#2b2b2b)" role="img" aria-label="Portrait of a sales partner"></div>
<p class="abs member-name" style="left:548px">Dana Whitlow</p>
<p class="abs member-role" style="left:548px">Sales Partner</p>

<div class="abs member-photo" style="left:741px;background:linear-gradient(180deg,#c9c9c9,#a9a6a2 55%,#6a5548)" role="img" aria-label="Portrait of a sales partner"></div>
<p class="abs member-name" style="left:741px">Dana Whitlow</p>
<p class="abs member-role" style="left:741px">Sales Partner</p>

<div class="abs member-photo" style="left:934px;background:linear-gradient(180deg,#3a2c24,#5a4a40 55%,#7a6e66)" role="img" aria-label="Portrait of a sales partner"></div>
<p class="abs member-name" style="left:934px">Dana Whitlow</p>
<p class="abs member-role" style="left:934px">Sales Partner</p>

<footer class="abs footer"></footer>

<h5 class="abs foot-head" style="left:100px">CONTACT US</h5>
<ul class="abs foot-list contact" style="left:98px;top:2053px">
  <li><svg width="12" height="12" viewBox="0 0 12 12"><path d="M2 1h3l1 3-2 1a7 7 0 0 0 3 3l1-2 3 1v3c-6 1-10-3-9-9z" fill="#26a9e8"/></svg>03 5550 0142 (Phone)</li>
  <li><svg width="12" height="12" viewBox="0 0 12 12"><rect x="1" y="4" width="10" height="6" fill="#26a9e8"/><rect x="3" y="1" width="6" height="3" fill="#26a9e8"/></svg>03 5550 0142 (Fax)</li>
  <li><svg width="12" height="12" viewBox="0 0 12 12"><rect x="1" y="2" width="10" height="8" fill="#26a9e8"/><path d="m1 2 5 4 5-4" fill="none" stroke="#14171c"/></svg><span style="text-decoration:underline">office@marlowtide.example</span></li>
  <li><svg width="12" height="12" viewBox="0 0 12 12"><path d="M6 11S2 6.5 2 4.5a4 4 0 0 1 8 0C10 6.5 6 11 6 11z" fill="#26a9e8"/><circle cx="6" cy="4.5" r="1.4" fill="#14171c"/></svg><span>PO Box 4410, Newport Coast<br>lorem si3844</span></li>
</ul>

<h5 class="abs foot-head" style="left:350px">TWITTER FEED</h5>
<div class="abs tweet" style="left:350px;top:2057px;width:215px">
  <p>@harborline, Harbor site theme full responsive is coming soon..<br><em>4 days ago</em></p>
  <p style="margin-top:10px">@harborline, Harbor site theme full responsive is coming soon..<br><em>4 days ago</em></p>
</div>

<h5 class="abs foot-head" style="left:666px">ABOUT</h5>
<ul class="abs foot-list about" style="left:665px;top:2046px">
  <li>Investors</li>
  <li>Careers</li>
  <li>Terms &amp; Condtions of Service</li>
  <li>Privacy Policy</li>
  <li>Service Level Agreement</li>
  <li>Master Commercial Agreement</li>
</ul>

<h5 class="abs foot-head" style="left:928px">FOLLOW US</h5>
<p class="abs tweet" style="left:928px;top:2057px;width:175px">Lorem ipsum dolor sit amet, consectetur adipiscing elit. Nulla in purus nibh. Donec ornare</p>
<div class="abs social" style="left:928px;top:2126px">
  <span></span><span class="on"></span><span></span><span></span><span></span>
</div>
<p class="abs copy">Copyright 2015 All Rights Reserved</p>

</body>
</html>
```